Veridane Works, Inc. - Update our Website

Veridane Works needs a website to help our customers to navigate through our services efficiently. Our existing website is at www.verowk.example

We would like to explain our services with content and pictures (photographs) that distinguishes our products and services from our competition.

The website design must implement a strategy to focus on our Contract Labeling services.

With this new design we would like to attract new customers and ensure that our existing customers are fully informed with our latest offerings.

```html
<!DOCTYPE html>
<html lang="en">
<head>
<meta charset="utf-8">
<title>Veridane Works, Inc.</title>
<link href="https://fonts.googleapis.com/css2?family=Exo+2:wght@400;700;800&family=Roboto:wght@400;500&display=swap" rel="stylesheet">
<style>
:root{
  --green:#7dc61e;
  --green-dark:#6cb012;
  --ink:#222;
  --text:#666;
  --muted:#999;
  --rule:#e3e3e3;
  --topbar:#111;
  --footer-bg:#fff;
  --bottom:#151515;
  --blue:#2a64b8;
}
*{margin:0;padding:0;box-sizing:border-box}
html,body{width:700px;height:1200px;overflow:hidden;background:#fff}
body{position:relative;font-family:"Roboto",Arial,sans-serif;color:var(--text)}
.topbar{position:absolute;top:0;left:0;width:700px;height:16px;background:var(--topbar);display:flex;justify-content:flex-end;align-items:center;gap:10px;padding-right:100px;font-size:6.5px;color:#bbb}
.topbar .dot{width:6px;height:6px;border-radius:50%;background:#777}
.topbar .sep{width:1px;height:10px;background:#333}
.topbar .item{display:flex;align-items:center;gap:4px}
.header{position:absolute;top:16px;left:0;width:700px;height:61px;border-bottom:1px solid #e6e6e6}
.brand{position:absolute;left:100px;top:17px;display:flex;align-items:center;gap:7px}
.brand-mark{width:30px;height:30px;border-radius:50%;background:var(--green)}
.brand-name{font-family:"Exo 2",sans-serif;font-weight:800;font-size:15px;color:var(--ink);letter-spacing:.3px;line-height:1}
.nav{position:absolute;right:100px;top:0;height:61px;display:flex;gap:24px;font-size:9px;color:var(--ink)}
.nav a{color:inherit;text-decoration:none;display:flex;align-items:center;position:relative}
.nav a.active{color:var(--green)}
.nav a.active::after{content:"";position:absolute;left:-4px;right:-4px;bottom:-1px;height:2px;background:var(--green)}
.hero{position:absolute;top:77px;left:0;width:700px;height:189px;background:linear-gradient(90deg,#eef3f4,#dfe8ea 55%,#e9eff0)}
.hero-photo{position:absolute;right:105px;top:0;width:200px;height:189px;background:linear-gradient(180deg,#e6ecef,#f4f6f7)}
.hero-title{position:absolute;left:100px;top:42px;font-family:"Exo 2",sans-serif;font-weight:800;font-size:21px;color:var(--green)}
.hero-text{position:absolute;left:100px;top:68px;width:245px;font-size:8.2px;line-height:1.3;color:#333}
.btn{display:inline-flex;align-items:center;justify-content:center;background:var(--green);color:#fff;font-size:7.5px;text-transform:uppercase;text-decoration:none}
.hero .btn{position:absolute;left:100px;top:118px;width:78px;height:28px}
.arrow{position:absolute;top:78px;width:28px;height:32px;background:rgba(120,120,120,.55);display:flex;align-items:center;justify-content:center}
.arrow.prev{left:0}.arrow.next{right:0}
.dots{position:absolute;left:340px;top:177px;display:flex;gap:3px}
.dots span{width:4px;height:4px;border-radius:50%;background:#bbb}
.dots span:first-child{background:#777}
.cards{position:absolute;top:295px;left:100px;width:500px;display:grid;grid-template-columns:245px 245px;column-gap:10px;row-gap:20px}
.card{height:214px;text-align:center}
.card-photo{height:105px;border:1px solid #ddd}
.card-title{font-family:"Exo 2",sans-serif;font-size:15.5px;color:var(--ink);margin-top:9px;height:22px}
.card-text{margin:6px 8px 0;padding:5px 0 6px;border-top:1px solid var(--rule);border-bottom:1px solid var(--rule);font-size:7px;line-height:1.35;color:var(--text);height:40px;padding-left:8px;padding-right:8px}
.card .btn{margin-top:9px;width:71px;height:28px}
.banner{position:absolute;top:997px;left:0;width:700px;height:66px;background:linear-gradient(90deg,#1f4f9a,#5c8fd3 45%,#2a64b8 75%,#3d78c6)}
.banner-title{position:absolute;right:100px;top:19px;font-family:"Exo 2",sans-serif;font-weight:800;font-size:21px;color:#fff}
.footer{position:absolute;top:1063px;left:0;width:700px;height:117px;background:var(--footer-bg)}
.col{position:absolute;top:17px}
.col h3{font-family:"Exo 2",sans-serif;font-weight:400;font-size:13px;color:var(--green);margin-bottom:7px}
.col ul{list-style:none;font-size:6.5px;color:#555}
.col li{line-height:12px}
.col li::before{content:"›";margin-right:5px;color:#444}
.col.menu{left:100px}.col.services{left:191px}.col.news{left:343px}
.email{display:flex;margin-top:0}
.email span{width:97px;height:22px;background:#e5e5e5;font-size:6px;color:#777;display:flex;align-items:center;padding-left:9px}
.email i{width:23px;height:22px;background:var(--green);display:flex;align-items:center;justify-content:center}
.social{display:flex;align-items:center;gap:8px;margin-top:13px}
.social h3{margin:0}
.social .circle{width:15px;height:15px;border-radius:50%}
.footer-mark{position:absolute;left:521px;top:16px;width:76px;height:76px;border-radius:50%;background:var(--green)}
.bottombar{position:absolute;top:1180px;left:0;width:700px;height:20px;background:var(--bottom);color:#aaa;font-size:7px;display:flex;align-items:center;justify-content:center}
</style>
</head>
<body>
<div class="topbar">
  <span class="dot"></span><span class="sep"></span><span class="dot"></span><span class="sep"></span>
  <span class="item"><svg width="7" height="7" viewBox="0 0 10 10"><path d="M2 1l2 2-1 1.5a6 6 0 0 0 2.5 2.5L7 6l2 2-1.5 1.5C4 9 1 6 .5 2.5z" fill="#bbb"/></svg>0800-555-0142</span>
  <span class="sep"></span>
  <span class="item"><svg width="8" height="6" viewBox="0 0 8 6"><rect width="8" height="6" fill="#bbb"/><path d="M0 0l4 3 4-3" stroke="#111" fill="none" stroke-width=".8"/></svg>VeridaneWorksINC.</span>
</div>

<header class="header">
  <div class="brand"><span class="brand-mark"></span><span class="brand-name">VERIDANE WORKS INC.</span></div>
  <nav class="nav"><a class="active" href="#">Home</a><a href="#">About</a><a href="#">Support</a><a href="#">Blog</a><a href="#">Contact</a></nav>
</header>

<section class="hero">
  <div class="hero-photo" role="img" aria-label="Doctor in a white coat holding a tablet in a bright clinic"></div>
  <h1 class="hero-title">VERIDANE WORKS, INC.</h1>
  <p class="hero-text">Veridane Works, Inc. specializes in providing products and services to the pharmaceutical industry. We are focused on the needs of those individuals involved with ClinicalTrial Materials. Our products and services are summarized.</p>
  <a class="btn" href="#">Read more</a>
  <span class="arrow prev"><svg width="8" height="14" viewBox="0 0 8 14"><path d="M7 1L1 7l6 6" stroke="#fff" fill="none" stroke-width="1.3"/></svg></span>
  <span class="arrow next"><svg width="8" height="14" viewBox="0 0 8 14"><path d="M1 1l6 6-6 6" stroke="#fff" fill="none" stroke-width="1.3"/></svg></span>
  <div class="dots"><span></span><span></span><span></span></div>
</section>

<main class="cards">
  <article class="card"><div class="card-photo" role="img" aria-label="Lab scientist working at a microscope" style="background:linear-gradient(135deg,#dfe6ec,#b9c6d2)"></div><h2 class="card-title">VeriServ™</h2><p class="card-text">VeriServ™ is a contract clinical label generation service that provides you with ready to apply clinical labels specifically designed and produced for your clinical...</p><a class="btn" href="#">Read more</a></article>
  <article class="card"><div class="card-photo" role="img" aria-label="Lab staff in caps working in a clean room" style="background:linear-gradient(135deg,#6fd08a,#cfe9dc)"></div><h2 class="card-title">VeriBook™</h2><p class="card-text">VeriBook™ labels are multi-page clinical labels used to address the needs of multi-language studies. This enables user to prepare and ship clinical materials to multiple...</p><a class="btn" href="#">Read more</a></article>
  <article class="card"><div class="card-photo" role="img" aria-label="Two doctors reviewing a clipboard" style="background:linear-gradient(135deg,#cfe0ee,#8fb3cf)"></div><h2 class="card-title">Clinical Randomizations</h2><p class="card-text">Our systems can create randomization data for all types of CTM requirements. Patient randomization, material randomization and random...</p><a class="btn" href="#">Read more</a></article>
  <article class="card"><div class="card-photo" role="img" aria-label="Stethoscope resting on a keyboard and clipboard" style="background:linear-gradient(135deg,#f2f2f2,#c9c9c9)"></div><h2 class="card-title">VeriPro/LBL™</h2><p class="card-text">VeriPro/LBL™ is the industry's leading clinical label generation system offering superior overall capability and flexibility The system enables users to...</p><a class="btn" href="#">Read more</a></article>
  <article class="card"><div class="card-photo" role="img" aria-label="Doctor and patient talking at a laptop" style="background:linear-gradient(135deg,#eceae4,#c8c6c0)"></div><h2 class="card-title">Software Validation Services</h2><p class="card-text">Veridane Works offers software validation services for the FDA regulated industry. Our knowledge of industry practices and standards...</p><a class="btn" href="#">Read more</a></article>
  <article class="card"><div class="card-photo" role="img" aria-label="Pharmacy worker sorting medicine packages" style="background:linear-gradient(135deg,#ece6e0,#bfb6ae)"></div><h2 class="card-title">VeriStock™</h2><p class="card-text">VeriStock™ is a premium line of label products that we supply to the pharmaceutical industry. These label stocks are specifically designed...</p><a class="btn" href="#">Read more</a></article>
</main>

<section class="banner" role="img" aria-label="Blue-toned close-up of a stethoscope on a keyboard">
  <div class="banner-title">VERIDANE WORKS, INC.</div>
</section>

<footer class="footer">
  <div class="col menu"><h3>MENU</h3><ul><li>Home</li><li>About</li><li>Support</li><li>Blog</li><li>Contact</li></ul></div>
  <div class="col services"><h3>SERVICES</h3><ul><li>VeriServ™</li><li>VeriBook™</li><li>Clinical Randomizations</li><li>VeriStock™</li><li>Software Validation Services</li></ul></div>
  <div class="col news"><h3>NEWSLETTER</h3>
    <div class="email"><span>EMAIL</span><i><svg width="11" height="9" viewBox="0 0 11 9"><path d="M1 4.5L10 1 7.5 8 5.5 5.5z" fill="none" stroke="#fff" stroke-width="1"/></svg></i></div>
    <div class="social"><h3>SOCIAL</h3><span class="circle" style="background:#3b5aa6"></span><span class="circle" style="background:#44a6dc"></span><span class="circle" style="background:#d64132"></span></div>
  </div>
  <div class="footer-mark"></div>
</footer>

<div class="bottombar">Northfield Design Network © 2014.</div>
</body>
</html>
```